Naturkosmetikpraxis sucht Design
Der Designer konnte gut meine Vorstellungen umsetzen und das in kürzester Zeit. Eine super Leistung, vor allem da ich weiß, dass es mir oft schwerfällt, mich klar auszudrücken.
Zielgruppe
Kosmetikpraxis, alle Altersgruppen aber Fokus Best Ager, vorwiegend weiblich, naturverbundene Menschen, gesundheitsbewusste Menschen, gestresste
gefallen soll es Menschen mit Hautproblemen und welchen, die einfach entspannen möchten.
Menschen, die Individualität suchen - nicht preiswerte Masse.
Aufgabenstellung
natürliche Hautpflegekonzepte,
Sugaring-Enthaarung, Wellness-Massagen, Naturnagelpflege, Wimpernlifting, Micro-Needling mit Lifting Pen, Klangschalenmassage, Permanent MakeUp
- Text mit Öffnungszeiten im Anhang "Banner..."
Als Farbe mag ich sehr dunkles rot, geht aber auch als Hintergrundfarbe. Ist wohl Brombeer etwa r171, g22, b78. Es geht ja hier um einen Banner für das Hoftor als Holz an einem Fachwerkhaus.
Habe noch ein paar Fotos aus meinem Bestand beigefügt.
Anderes Bild natürlich auch o.k.
BILD: 48193527 Frau m. Freesie von Bildarix. Das anhängende Bild flieder bluete 71846302 geht in eine ganz andere Richtung, ich weiß. Aber es ist ein tolles Bild und ich wäre durchaus bereit, auf flieder im Design zu wechseln. 08.04.14: jetzt hat sich das LOGO doch verändert.

```html
<!DOCTYPE html>
<html lang="de">
<head>
<meta charset="utf-8">
<title>Kosmetikpraxis Lena Hofstetter – Banner</title>
<link href="https://fonts.googleapis.com/css2?family=Arimo:wght@400&family=Italianno&display=swap" rel="stylesheet">
<style>
  :root {
    --berry: #ab164e;
    --berry-deep: #9c1246;
    --white: #ffffff;
    --rule: rgba(255,255,255,0.92);
    --skin-light: #e2b08c;
    --skin-mid: #c98a62;
    --skin-dark: #7a4a32;
  }
  * { margin: 0; padding: 0; box-sizing: border-box; }
  html, body { width: 1200px; height: 2799px; overflow: hidden; background: var(--berry); }
  .banner {
    position: relative;
    width: 1200px;
    height: 2799px;
    background: linear-gradient(180deg, var(--berry) 0%, var(--berry) 60%, var(--berry-deep) 100%);
    color: var(--white);
    font-family: "Arimo", Arial, sans-serif;
    overflow: hidden;
  }
  .brand {
    position: absolute;
    top: 190px;
    left: 0;
    width: 100%;
    display: flex;
    justify-content: center;
    align-items: center;
    gap: 26px;
  }
  .brand-dot {
    width: 34px; height: 34px;
    border-radius: 50%;
    background: var(--white);
  }
  .brand-name {
    font-family: "Arimo", Arial, sans-serif;
    font-size: 82px;
    font-weight: 400;
    letter-spacing: 2px;
    color: var(--white);
  }
  .hero {
    position: absolute;
    top: 370px;
    left: 0;
    width: 1200px;
    height: 1270px;
  }
  .rule {
    position: absolute;
    left: 126px;
    width: 954px;
    height: 5px;
    background: var(--rule);
    box-shadow: 0 2px 6px rgba(0,0,0,0.25);
  }
  .rule--top { top: 1693px; }
  .rule--bottom { top: 2045px; }
  .title {
    position: absolute;
    top: 1730px;
    left: 0;
    width: 100%;
    text-align: center;
    font-family: "Italianno", cursive;
    font-size: 196px;
    line-height: 1;
    font-weight: 400;
  }
  .owner {
    position: absolute;
    top: 1968px;
    left: 0;
    width: 100%;
    text-align: center;
    font-size: 50px;
    line-height: 1;
  }
  .services, .hours {
    position: absolute;
    left: 0;
    width: 100%;
    list-style: none;
    text-align: center;
    font-size: 31px;
    line-height: 42px;
  }
  .services { top: 2120px; }
  .hours { top: 2410px; }
</style>
</head>
<body>
<main class="banner">
  <header class="brand">
    <span class="brand-dot"></span>
    <span class="brand-name">Lunavera</span>
  </header>

  <svg class="hero" viewBox="0 0 1200 1270" width="1200" height="1270" role="img" aria-label="Foto: Frau bei einer Hot-Stone-Massage mit Orchideen und Pflegecreme">
    <defs>
      <linearGradient id="heroFill" x1="0" y1="0" x2="1" y2="1">
        <stop offset="0" stop-color="var(--skin-light)"/>
        <stop offset="0.55" stop-color="var(--skin-mid)"/>
        <stop offset="1" stop-color="var(--skin-dark)"/>
      </linearGradient>
    </defs>
    <path d="M0 52 Q600 -20 1200 52 L1200 1200 Q600 1290 0 1200 Z" fill="url(#heroFill)" stroke="var(--white)" stroke-width="5"/>
  </svg>

  <div class="rule rule--top"></div>
  <h1 class="title">Kosmetikpraxis</h1>
  <p class="owner">Lena Hofstetter</p>
  <div class="rule rule--bottom"></div>

  <ul class="services">
    <li>Natürliche Hautpflegekonzepte</li>
    <li>Wellness-Massagen</li>
    <li>Micro-Needling Lifting Pen</li>
    <li>Naturnagelpflege</li>
    <li>Permanent MakeUp</li>
    <li>Beratung und Verkauf</li>
  </ul>

  <ul class="hours">
    <li>Öffnungszeiten</li>
    <li>MO 15 - 19 Uhr nur Verkauf</li>
    <li>DI, MI, FR 9.30 - 13 Uhr, 14 - 18 Uhr</li>
    <li>DO 14 - 20 Uhr</li>
    <li>SA 10 - 13 Uhr</li>
    <li>Tel. 06150 482731</li>
    <li>www.kosmetikpraxis-hofstetter.de</li>
    <li>info@naturkosmetik-lindenau.de</li>
  </ul>
</main>
</body>
</html>
```